Divorce Lawyer print and ebook cover (Lanterns over the quiet harbor )

I need a front and back cover for my divorce and family law book. I already have a photo and title. The back cover photo is not necessary but can be interesting the Front-main cover is a must

Target Market(s)

Prospective client

Colors

Designer to choose colors to be used in the design.

Requirements
Must have
• Front photo by viewable.

```html
<!DOCTYPE html>
<html lang="en">
<head>
<meta charset="utf-8">
<title>Lanterns over the quiet harbor — Cover</title>
<link rel="stylesheet" href="https://fonts.googleapis.com/css2?family=Bebas+Neue&display=swap">
<style>
  :root {
    --stage: #7a8d9b;
    --title-panel-light: #f1f1ef;
    --title-panel-mid: #e2e2df;
    --ink: #08090a;
    --author-band: #c9b49b;
    --photo-cool: #2f3d4a;
    --photo-mist: #b9c7cf;
    --photo-warm: #d9b85a;
    --photo-green: #9cb35a;
    --road: #3a3d40;
  }
  * { box-sizing: border-box; margin: 0; padding: 0; }
  html, body {
    width: 1200px;
    height: 1200px;
    overflow: hidden;
    background: var(--stage);
  }
  .canvas {
    width: 1200px;
    height: 1200px;
    display: flex;
    align-items: center;
    justify-content: center;
  }
  .book-cover {
    width: 729px;
    height: 1100px;
    display: flex;
    flex-direction: column;
    box-shadow: 0 10px 40px rgba(0, 0, 0, 0.25);
  }
  .title-panel {
    height: 388px;
    background:
      radial-gradient(circle at 30% 35%, var(--title-panel-light), var(--title-panel-mid) 75%);
    display: flex;
    flex-direction: column;
    align-items: center;
    justify-content: center;
    gap: 6px;
    padding-top: 10px;
  }
  .book-title {
    font-family: "Bebas Neue", "Arial Narrow", sans-serif;
    color: var(--ink);
    text-align: center;
    line-height: 0.95;
    font-weight: 400;
  }
  .book-title .title-main {
    display: block;
    font-size: 122px;
    letter-spacing: 1px;
  }
  .book-title .title-sub {
    display: block;
    font-size: 96px;
    letter-spacing: 1px;
  }
  .cover-photo {
    height: 553px;
    background:
      linear-gradient(180deg, rgba(255,255,255,0.35) 0%, rgba(255,255,255,0) 40%, rgba(0,0,0,0) 60%, var(--road) 100%),
      linear-gradient(90deg, var(--photo-cool) 0%, var(--photo-mist) 45%, var(--photo-warm) 72%, var(--photo-green) 100%);
  }
  .author-band {
    height: 159px;
    background: var(--author-band);
    display: flex;
    align-items: center;
    justify-content: center;
  }
  .author-name {
    font-family: "Bebas Neue", "Arial Narrow", sans-serif;
    font-size: 86px;
    color: var(--ink);
    letter-spacing: 1px;
    line-height: 1;
    padding-top: 6px;
  }
</style>
</head>
<body>
  <main class="canvas">
    <article class="book-cover">
      <header class="title-panel">
        <h1 class="book-title">
          <span class="title-main">LANTERNS OVER</span>
          <span class="title-sub">THE QUIET HARBOR</span>
        </h1>
      </header>
      <div class="cover-photo" role="img" aria-label="Photo of a man in a dark suit, seen from behind, standing at a fork in a misty forest road; a signpost points left to a bare, grey path marked Old Life and right to a sunlit, green path marked New Life"></div>
      <footer class="author-band">
        <p class="author-name">AUTHOR NAME</p>
      </footer>
    </article>
  </main>
</body>
</html>
```